Mistvale Botanica Teas needs a website with shopping cart

We are a herbal tea business that hand blends organic tea recipes for medicinal purposes and for customer enjoyment. We require a website that represents our elegant brand and our connection to plant medicine. We will require a home page, a products page, a contact us page with form and an information page. We will need to be able to photograph our teas and upload the images to the products page along with changing pricing and shipping costs, and the ability to add/change information and images to our information page as this page will be mostly about the different herbs we will use in the teas. Our teas will be 'loose leaf' (not in tea bags) and will be sold in glass jars. At this stage we only intend to use CoinLoop as a method of payment for overseas customers and direct credit for New Zealand customers.

Target Market(s)

Tea drinkers, women, people interested in health/herbs, people looking for gifts

Industry/Entity Type

Shopping

Logo Text

Mistvale Botanica Teas

Coding

Coded - Design and coding required

Number of Pages Required

4 page

Font styles to use
Decorative

Requirements
Must have
• I am a herbalist and love plants, flowers and nature so would like the overall website and logo to represent this. I have attached the logo I had designed several years ago for myself as inspiration - the graduated greens are great and very vibrant which I like (sorry about the quality, I couldn't find the source files - NEW SOURCE FILE ADDED 23/04/15). This is an upmarket, niche product which is elegant and healthy.

```html
<!DOCTYPE html>
<html lang="en">
<head>
<meta charset="utf-8">
<title>Mistvale Botanica Teas</title>
<link rel="stylesheet" href="https://fonts.googleapis.com/css2?family=Marcellus&family=Dancing+Script:wght@600;700&family=Playfair+Display:ital,wght@1,700&family=Lora:ital,wght@0,400;1,400;1,600&family=Open+Sans:wght@400;600;700&family=Crimson+Text&display=swap">
<style>
  :root{
    --paper:#f1f0e8;
    --panel-light:#efe3b0;
    --panel-dark:#d9c580;
    --green:#2f9a1e;
    --green-deep:#237a12;
    --green-bright:#44b82a;
    --lime:#8cc63f;
    --band:#d6c96f;
    --band-dark:#c9b95a;
    --ink:#222;
    --white:#fff;
  }
  *{box-sizing:border-box;margin:0;padding:0}
  html,body{width:1200px;height:1200px;overflow:hidden}
  body{position:relative;background:linear-gradient(180deg,#f4f3ec 0%,var(--paper) 60%);font-family:"Open Sans",sans-serif;color:var(--ink)}
  .abs{position:absolute}

  .leaf-canopy{left:0;top:0;width:1200px;height:50px;background:linear-gradient(180deg,#7cbf4a 0%,rgba(150,205,100,.55) 55%,rgba(241,240,232,0) 100%)}

  .herb-strip{left:100px;top:350px;width:1000px;height:100px;background:linear-gradient(90deg,#6aa83c 0%,#cfe2b0 12%,#d83a2a 38%,#8a6bc0 46%,#e0b030 58%,#4caf3a 70%,#e8e4d8 80%,#6ab04a 92%,#f0efe6 100%);opacity:.85;border-radius:2px}
  .hero-paper{left:408px;top:130px;width:692px;height:220px;background:linear-gradient(180deg,#f3f1e6,#ecebdf)}

  .side-panel{left:142px;top:0;width:266px;height:450px;background:linear-gradient(90deg,var(--panel-dark) 0%,var(--panel-light) 20%,var(--panel-light) 80%,var(--panel-dark) 100%);border-left:2px solid #c9b46a;border-right:2px solid #c9b46a;box-shadow:0 2px 6px rgba(0,0,0,.15)}
  .side-panel .curl{position:absolute;left:-2px;bottom:-8px;width:266px;height:12px;border-radius:0 0 50% 50%;background:var(--green-bright)}
  .brand{position:absolute;left:0;top:48px;width:100%;text-align:center}
  .brand-mark{display:inline-block;width:44px;height:44px;border-radius:50%;background:var(--green)}
  .brand-name{font-family:"Marcellus",serif;font-size:19px;color:var(--green-deep);margin-top:16px;letter-spacing:.5px}
  .brand-role{font-family:"Open Sans",sans-serif;font-size:7.5px;color:var(--green-deep);letter-spacing:.6px;margin-top:4px}
  .side-nav{position:absolute;left:32px;top:188px;width:210px;list-style:none}
  .side-nav li{height:37px;border-bottom:1px dashed #a8925a;display:flex;align-items:center;font-family:"Marcellus",serif;font-size:21px;color:var(--green)}
  .side-nav li:last-child{border-bottom:none}
  .side-nav svg{margin-right:10px}

  .account{left:788px;top:48px;font-family:"Lora",serif;font-style:italic;font-size:14px;display:flex;gap:14px;color:var(--ink)}
  .account .guest{color:var(--green-deep);margin-left:10px}
  .cart-badge{left:1022px;top:38px;width:38px;height:38px;border-radius:50%;background:#dfe4c6;border:2px solid #c8d0a4;display:flex;align-items:center;justify-content:center;font-size:12px;font-weight:700;color:var(--green-deep)}

  .top-nav{left:432px;top:96px;width:346px;height:32px;border-radius:16px;background:linear-gradient(180deg,#f1e7bd,#ddcd8c);display:flex;align-items:center;gap:20px;padding:0 14px;font-family:"Lora",serif;font-style:italic;font-size:13px;color:#333}
  .top-nav span{display:flex;align-items:center;gap:5px}
  .top-nav b{font-family:"Open Sans",sans-serif;font-style:normal;font-weight:600;font-size:14px}
  .search{left:790px;top:96px;width:270px;height:32px;border-radius:16px;background:#fff;border:2px solid #ddcd8c;display:flex;overflow:hidden}
  .search .field{flex:1;padding:6px 12px;font-family:"Lora",serif;font-style:italic;font-size:13px;color:#a89a6c}
  .search .btn{width:70px;background:linear-gradient(180deg,#efe4b6,#d8c885);font-family:"Lora",serif;font-style:italic;font-size:14px;display:flex;align-items:center;justify-content:center;color:#333}

  .hero-kicker{left:460px;top:140px;font-family:"Dancing Script",cursive;font-weight:600;font-size:40px;color:#5a6a52}
  .hero-title{left:630px;top:192px;font-family:"Dancing Script",cursive;font-weight:700;font-size:60px;color:var(--green-bright)}
  .hero-copy{left:462px;top:266px;width:604px;font-family:"Lora",serif;font-style:italic;font-size:15px;line-height:20px;color:var(--green-deep)}
  .hero-copy strong{font-weight:600;display:block}

  .section-title{left:101px;top:484px;font-family:"Playfair Display",serif;font-style:italic;font-weight:700;font-size:31px;color:var(--green)}
  .fresh{left:374px;top:496px;font-size:13px;display:flex;align-items:center;gap:8px}

  .arrow{top:634px;width:0;height:0;border-top:7px solid transparent;border-bottom:7px solid transparent}
  .arrow.prev{left:84px;border-right:11px solid #999}
  .arrow.next{left:1104px;border-left:11px solid #999}
  .product{top:546px;width:232px}
  .product.last{width:220px}
  .product .photo{height:186px;background:var(--white);display:flex;align-items:center;justify-content:center}
  .product .tea{width:154px;height:154px;border-radius:6px;background:radial-gradient(circle,#c9a24a 0%,#a8853a 45%,#f6f0da 72%)}
  .product .name{text-align:center;font-size:16px;margin-top:10px;letter-spacing:.3px}
  .product .buy{display:flex;justify-content:center;align-items:center;gap:12px;margin-top:6px}
  .product .price{font-weight:700;font-size:16px}
  .product .btn{background:var(--lime);color:#fff;font-weight:700;font-size:15px;padding:3px 12px;border:1px solid #6ea52c;letter-spacing:.5px}

  .footer-band{left:0;top:840px;width:1200px;height:360px;background:linear-gradient(180deg,var(--band) 0%,#ddd07b 50%,var(--band-dark) 100%)}
  .stamp{top:842px;width:256px;height:176px;background:var(--green);border:6px dotted var(--band);text-align:center;color:#fff;font-family:"Lora",serif;font-style:italic}
  .stamp .disc{width:94px;height:94px;border-radius:50%;background:#fff;border:4px solid var(--green-bright);margin:6px auto 0;display:flex;align-items:center;justify-content:center}
  .stamp h3{font-weight:400;font-size:16px;margin-top:14px}
  .stamp p{font-size:11px;margin-top:3px}
  .cards{display:inline-flex;align-items:center;gap:3px;background:#fff;padding:2px 4px;margin-top:4px}
  .cards i{display:block;width:18px;height:11px}
  .cards em{font-family:"Open Sans",sans-serif;font-style:normal;font-size:9px;font-weight:700;color:#1b3a80;margin-left:2px}

  .footer-links{top:1064px;list-style:none;font-family:"Crimson Text",serif;font-size:16px;color:#222}
  .footer-links li{height:30px}
  .social{left:870px;top:1036px;width:206px;height:92px;border-radius:10px;background:linear-gradient(160deg,#8fd45e,#3a9a22);display:flex;align-items:center;justify-content:center}
  .social span{color:#fff;font-family:"Open Sans",sans-serif;font-weight:700;font-size:18px}
  .like{left:864px;top:1154px;display:flex;align-items:center;gap:8px;font-family:"Lora",serif;font-style:italic;font-weight:600;font-size:15px;color:#2a4aa0}
  .like i{display:block;width:20px;height:20px;background:#3b5aa8}
</style>
</head>
<body>

<div class="abs leaf-canopy" role="img" aria-label="Hanging green leaves along the top edge"></div>
<div class="abs hero-paper"></div>
<div class="abs herb-strip" role="img" aria-label="Aloe, hibiscus flower, lavender, turmeric roots, capsule, mortar and pestle and mint leaves"></div>

<aside class="abs side-panel">
  <div class="brand">
    <span class="brand-mark"></span>
    <div class="brand-name">MISTVALE BOTANICA TEAS</div>
    <div class="brand-role">• NATUROPATH, MEDICAL HERBALIST &amp; NUTRITIONIST •</div>
  </div>
  <ul class="side-nav">
    <li><svg width="26" height="14" viewBox="0 0 26 14"><ellipse cx="13" cy="7" rx="12" ry="5" fill="#3f9a1c"/></svg>Suppliments</li>
    <li><svg width="26" height="14" viewBox="0 0 26 14"><ellipse cx="13" cy="7" rx="12" ry="5" fill="#3f9a1c"/></svg>Skin Care</li>
    <li><svg width="26" height="14" viewBox="0 0 26 14"><ellipse cx="13" cy="7" rx="12" ry="5" fill="#3f9a1c"/></svg>Our Retailers</li>
    <li><svg width="26" height="14" viewBox="0 0 26 14"><ellipse cx="13" cy="7" rx="12" ry="5" fill="#3f9a1c"/></svg>Articles</li>
    <li><svg width="26" height="14" viewBox="0 0 26 14"><ellipse cx="13" cy="7" rx="12" ry="5" fill="#3f9a1c"/></svg>About us</li>
    <li><svg width="26" height="14" viewBox="0 0 26 14"><ellipse cx="13" cy="7" rx="12" ry="5" fill="#3f9a1c"/></svg>Register/ Enquiry</li>
  </ul>
  <span class="curl"></span>
</aside>

<div class="abs account"><span>Login</span><span>Register</span><span class="guest">Welcome Guest</span></div>
<div class="abs cart-badge">3</div>

<nav class="abs top-nav">
  <span><svg width="14" height="12" viewBox="0 0 14 12"><path d="M7 0L0 6h2v6h4V8h2v4h4V6h2z" fill="#7a6a3a"/></svg>Home</span>
  <span><svg width="18" height="12" viewBox="0 0 18 12"><rect x="0" y="1" width="18" height="11" fill="#7a6a3a"/><path d="M0 1l9 6 9-6" stroke="#f1e7bd" fill="none"/></svg>Contact</span>
  <span><svg width="14" height="14" viewBox="0 0 14 14"><path d="M3 0l3 3-2 2c1 2 3 4 5 5l2-2 3 3-2 3C6 14 0 8 0 3z" fill="#7a6a3a"/></svg>Call <b>555.555.5555</b></span>
</nav>
<div class="abs search"><div class="field">What are you looking for</div><div class="btn">Search</div></div>

<div class="abs hero-kicker">Your Journey to</div>
<div class="abs hero-title">Natural Living!</div>
<p class="abs hero-copy">All Greenhollow Apothecary Suppliments and Skincare Producs are made with strick adherence to true and ancient time tested formulas, all with an excellent track record. All products are designed to be condition specific and are standardized multi herb formulas.<strong>Read more on these or call 555-555-5555 today!</strong></p>

<h2 class="abs section-title">Featured Products</h2>
<div class="abs fresh"><svg width="18" height="12" viewBox="0 0 18 12"><ellipse cx="9" cy="6" rx="8" ry="5" fill="#44b82a"/></svg>Guranteed Fresh Products!</div>

<span class="abs arrow prev"></span>
<span class="abs arrow next"></span>

<div class="abs product" style="left:97px">
  <div class="photo"><div class="tea" role="img" aria-label="Loose dried herbal tea blend"></div></div>
  <div class="name">Turmeric Curcumin</div>
  <div class="buy"><span class="price">$24.99</span><span class="btn">Buy Now</span></div>
</div>
<div class="abs product" style="left:353px">
  <div class="photo"><div class="tea" role="img" aria-label="Loose dried herbal tea blend"></div></div>
  <div class="name">Blood Sugar Suppliments</div>
  <div class="buy"><span class="price">$24.99</span><span class="btn">Buy Now</span></div>
</div>
<div class="abs product" style="left:614px">
  <div class="photo"><div class="tea" role="img" aria-label="Loose dried herbal tea blend"></div></div>
  <div class="name">Pomegranate Suppliments</div>
  <div class="buy"><span class="price">$19.99</span><span class="btn">Buy Now</span></div>
</div>
<div class="abs product last" style="left:877px">
  <div class="photo"><div class="tea" role="img" aria-label="Loose dried herbal tea blend"></div></div>
  <div class="name">Stress Suppliments</div>
  <div class="buy"><span class="price">$20.00</span><span class="btn">Buy Now</span></div>
</div>

<div class="abs footer-band"></div>

<div class="abs stamp" style="left:102px">
  <div class="disc" role="img" aria-label="Yellow delivery truck"><svg width="60" height="36" viewBox="0 0 60 36"><rect x="2" y="4" width="36" height="22" fill="#f2b705"/><path d="M38 10h12l8 8v8H38z" fill="#f2b705"/><circle cx="14" cy="29" r="5" fill="#333"/><circle cx="48" cy="29" r="5" fill="#333"/></svg></div>
  <h3>Free Shipping</h3>
  <p>on orders of $20 or more</p>
</div>
<div class="abs stamp" style="left:473px">
  <div class="disc"><div role="img" aria-label="Loose dried herbal tea blend" style="width:84px;height:84px;border-radius:50%;background:radial-gradient(circle,#c9a24a,#8f6e2c)"></div></div>
  <h3>Testimonials &amp; Reviews</h3>
  <p>Watch Videos</p>
</div>
<div class="abs stamp" style="left:844px">
  <div class="disc"><div style="width:74px;height:74px;border-radius:50%;background:#e8c64a;border:3px solid #b59220"></div></div>
  <h3>Secured Payment</h3>
  <div class="cards"><i style="background:#1a3f8f"></i><i style="background:#d9531e"></i><i style="background:#3b7cc4"></i><em>CoinLoop</em></div>
</div>

<ul class="abs footer-links" style="left:102px"><li>Home</li><li>Suppliments</li><li>Skin Care</li><li>About Us</li></ul>
<ul class="abs footer-links" style="left:302px"><li>Our Retailors</li><li>Payments</li><li>Returns</li><li>Shipping Rates &amp; Information</li></ul>
<ul class="abs footer-links" style="left:628px"><li>FAQ</li><li>Help/Customer Support</li><li>Terms of Use</li><li>Privacy Policy</li></ul>

<div class="abs social" role="img" aria-label="Green leaf graphic linking to the social page"><span>Find us on Leafnet</span></div>
<div class="abs like"><i></i>Like Us &amp; Get Informed!</div>

</body>
</html>
```